International Trading Company, 'ZORLIK' needs a Business Card

The company name is "ZORLIK" and it has own logo design.
I'd like to use its logo on this business card.
I need two side Business Card.
I'll look forward to your great design.
Thank you very much in advance.

Contact Information for Business Card

Company Name : Zorlik Harbour Limited
Information Example
Dorian Pallister
Mobile(use icon please) : 1 (212) 555-0143
Tel(use icon please) : 1 (212) 555-0178
Email(use icon please) : dorian27@kiroharbour-mail.com
Address(use icon please) : 482 Halden Ave, New York, NY 10160, USA

```html
<!DOCTYPE html>
<html lang="en">
<head>
<meta charset="utf-8">
<title>Zorlik Harbour Limited – Business Card</title>
<link rel="stylesheet" href="https://fonts.googleapis.com/css2?family=Arimo:wght@400;700&display=swap">
<style>
  :root {
    --backdrop: #2b2b2b;
    --slate: #5c5c5c;
    --slate-deep: #4f4f4f;
    --band-light: #e6e6e6;
    --band-shade: #cfcfcf;
    --rule: #d9d9d9;
    --ink: #1f1f1f;
    --ink-soft: #5a5a5a;
    --address: #9c9c9c;
    --white: #ffffff;
  }
  * { box-sizing: border-box; margin: 0; padding: 0; }
  html, body {
    width: 1200px; height: 997px; overflow: hidden;
    background: var(--backdrop);
    font-family: "Arimo", Arial, sans-serif;
  }
  .stage { position: relative; width: 1200px; height: 997px; }

  .card {
    position: absolute;
    width: 620px; height: 354px;
    background: linear-gradient(180deg, var(--slate), var(--slate-deep));
    box-shadow: 0 10px 30px rgba(0,0,0,.45);
    overflow: hidden;
  }
  .card--front { left: 90px; top: 90px; }
  .card--back  { left: 490px; top: 540px; }

  .band {
    position: absolute; left: 0; right: 0;
    background: linear-gradient(180deg, var(--band-light), var(--band-shade));
  }
  .rule {
    position: absolute; left: 0; right: 0; height: 2px;
    background: var(--rule);
  }

  .brand-name {
    position: absolute;
    color: var(--white);
    font-weight: 700;
    letter-spacing: 2px;
    line-height: 1;
    white-space: nowrap;
  }

  /* front */
  .card--front .brand-name { left: 60px; top: 102px; font-size: 112px; }
  .card--front .rule--upper { top: 228px; }
  .card--front .band { top: 238px; height: 78px; }
  .card--front .rule--lower { top: 324px; }
  .website {
    position: absolute; left: 150px; top: 268px;
    font-size: 15px; letter-spacing: 4px; color: var(--ink-soft);
    white-space: nowrap;
  }

  /* back */
  .card--back .brand-name { right: 70px; top: 54px; font-size: 66px; }
  .card--back .rule--upper { top: 148px; }
  .card--back .band { top: 158px; height: 128px; }
  .card--back .rule--lower { top: 294px; }
  .person { position: absolute; left: 40px; top: 222px; }
  .person-name { font-size: 20px; font-weight: 700; color: var(--ink); letter-spacing: .5px; white-space: nowrap; }
  .person-title { font-size: 15px; font-weight: 700; color: var(--ink-soft); margin-left: 78px; margin-top: 2px; }
  .divider {
    position: absolute; left: 316px; top: 176px; width: 2px; height: 90px;
    background: linear-gradient(180deg, transparent, #3a3a60, transparent);
  }
  .contacts { position: absolute; left: 336px; top: 176px; list-style: none; }
  .contacts li {
    display: flex; align-items: center; gap: 10px;
    font-size: 15px; color: var(--ink); height: 28px; white-space: nowrap;
  }
  .contact-icon { width: 18px; height: 18px; flex: none; }
  .address {
    position: absolute; left: 0; right: 0; top: 312px;
    text-align: center; font-size: 16px; color: var(--address); letter-spacing: .5px;
  }
</style>
</head>
<body>
<main class="stage">

  <section class="card card--front" aria-label="Business card front">
    <div class="brand-name">ZORLIK</div>
    <div class="rule rule--upper"></div>
    <div class="band"></div>
    <div class="rule rule--lower"></div>
    <p class="website">www.zorlikharbour-mail.com</p>
  </section>

  <section class="card card--back" aria-label="Business card back">
    <div class="brand-name">ZORLIK</div>
    <div class="rule rule--upper"></div>
    <div class="band"></div>
    <div class="rule rule--lower"></div>

    <div class="person">
      <p class="person-name">DORIAN PALLISTER</p>
      <p class="person-title">Director</p>
    </div>

    <div class="divider"></div>

    <ul class="contacts">
      <li>
        <svg class="contact-icon" viewBox="0 0 18 18" aria-label="Mobile">
          <circle cx="9" cy="9" r="9" fill="#555"/>
          <rect x="6" y="4" width="6" height="10" rx="1" fill="#eee"/>
          <rect x="7" y="5.5" width="4" height="6" fill="#555"/>
        </svg>
        1 (212) 555-0143
      </li>
      <li>
        <svg class="contact-icon" viewBox="0 0 18 18" aria-label="Telephone">
          <circle cx="9" cy="9" r="9" fill="#555"/>
          <path d="M5 7c0-1.5 1.5-2.5 4-2.5S13 5.5 13 7l-1.8.6-.5-1.3H7.3l-.5 1.3z" fill="#eee"/>
          <rect x="5.5" y="9" width="7" height="4" rx="1" fill="#eee"/>
        </svg>
        1 (212) 555-0178
      </li>
      <li>
        <svg class="contact-icon" viewBox="0 0 18 18" aria-label="Email">
          <circle cx="9" cy="9" r="9" fill="#555"/>
          <rect x="4.5" y="5.5" width="9" height="7" fill="#eee"/>
          <path d="M4.5 5.5L9 9.5l4.5-4" fill="none" stroke="#555" stroke-width="1"/>
        </svg>
        dorian27@zorlikharbour-mail.com
      </li>
    </ul>

    <p class="address">482 Halden Ave, New York, NY 10160, USA</p>
  </section>

</main>
</body>
</html>
```